Visitenkarten-Design für virtuelle Jobmesse & Jobbörse für Soldaten
Zielgruppe
Die KLO GmbH ist ein Unternehmen das zwei Hauptprodukte betreibt! Zum einen Jobbörse für Soldaten unter www.wachwechselpunkt.de und zum anderen eine virtuelle Jobmesse für Soldaten unter www.marvento.de , die wir zweimal im Jahr veranstalten.
Aufgabenstellung
Wir haben ja die beiden Produkte Wachwechselpunkt.de und die Marvento, für die bereits jeweils ein separtes Logo besteht! Diese finden Sie im Anhang! Beide werden doch jedoch von einem Unternehmen, der KLO GmbH betrieben! Aktuell nutzen wir eine Visitenkarte mit dem Logo von KLO und eine mit dem Logo der MARVENTO. Gerade im Hinblick darauf, dass wir zukünftig auch weiter Plattformen in unser Portfolio aufnehmen, möchte ich hier unsere V-Karten flexibler gestalten!
Ziel soll es also sein, eine Visitenkarte zu gestalten, auf dem klar wird, dass der Mitarbeiter von der KLO GmbH kommt, die KLO GmbH aber unterschiedliche Produkte betreibt.
Im Anhang finden Sie:
1. Das Logo von KLO
2. Das Logo von Marvento
3. Die aktuelle V-Karte von KLO
4. Die aktuelle V-Karte von MARVENTO
Vielleicht ein kleiner Anreiz: Aktuell nutzen wir auch zwei getrennte Geschäftspapiere. Das von www.wachwechselpunkt.de lade ich einmal hoch! Der Designer, der auch die Visitenkarte erstellt, erhällt im Anschluss den 1:1 Auftrag in Höhe von 200 Euro für die Erstellung des Geschäftspapiers! Wenn Sie jetzt schon einen Vorschlag für das Geschäftspapier einreichen, erhöht das natürlich Ihre Chancen, wobei ich verspreche, dass wir im Falle eine Annahme das 1:1 im Anschluß dennoch starten werden!

```html
<!DOCTYPE html>
<html lang="de">
<head>
<meta charset="utf-8">
<title>Visitenkarte KLO GmbH</title>
<link href="https://fonts.googleapis.com/css2?family=Arimo:ital,wght@0,400;0,700;1,400&display=swap" rel="stylesheet">
<style>
  :root {
    --bg: #2a2a2a;
    --card-white: #ffffff;
    --card-dark: #252525;
    --brand-blue: #2c4a8e;
    --brand-grey: #8a8a8a;
    --brand-green: #41592b;
    --brand-green-light: #5a7a3c;
    --text-dark: #3a3a3a;
    --text-light: #e8e8e8;
  }
  * { margin: 0; padding: 0; box-sizing: border-box; }
  html, body { width: 1200px; height: 801px; overflow: hidden; }
  body {
    background: var(--bg);
    font-family: "Arimo", Arial, sans-serif;
    position: relative;
  }
  .card {
    position: absolute;
    top: 226px;
    width: 540px;
    height: 349px;
    overflow: hidden;
    box-shadow: 0 10px 30px rgba(0,0,0,.45);
  }
  .card--front { left: 40px; background: var(--card-white); }
  .card--back { left: 620px; background: var(--card-dark); }

  .rule { position: absolute; height: 3px; }
  .rule--blue { background: var(--brand-blue); }
  .rule--grey { background: var(--brand-grey); height: 2px; }

  /* front */
  .front-brand {
    position: absolute; left: 30px; top: 62px; width: 170px;
    text-align: center;
  }
  .front-brand__mark { font-size: 17px; color: var(--brand-blue); }
  .front-brand__company {
    margin-top: 12px; font-size: 24px; font-weight: 700; color: var(--text-dark);
  }
  .person { position: absolute; left: 238px; top: 48px; }
  .person__name { font-size: 26px; color: var(--brand-blue); }
  .person__title { font-size: 13px; color: var(--text-dark); margin-top: 2px; }
  .address {
    position: absolute; left: 268px; top: 122px;
    font-size: 13px; line-height: 18px; color: var(--text-dark);
  }
  .contact {
    position: absolute; left: 268px; top: 186px;
    font-size: 12px; line-height: 18px; color: var(--text-dark);
    border-collapse: collapse;
  }
  .contact td { padding: 0 8px 0 0; }
  .contact__label { color: var(--brand-blue); }
  .contact__label--green { color: var(--brand-green); }
  .sub-brand {
    position: absolute; left: 30px; top: 222px; width: 200px; text-align: center;
  }
  .sub-brand__mark {
    display: inline-flex; align-items: center; gap: 8px;
    font-size: 18px; color: var(--brand-green);
  }
  .sub-brand__dot { width: 12px; height: 12px; border-radius: 50%; background: var(--brand-green); }
  .sub-brand__site { margin-top: 8px; font-size: 16px; font-weight: 700; color: var(--brand-green); }
  .sub-brand__note { margin-top: 6px; font-size: 10px; font-style: italic; color: var(--text-dark); }

  /* back */
  .back-brand {
    position: absolute; left: 0; right: 0; top: 96px; text-align: center;
    font-size: 26px; color: var(--text-light); letter-spacing: 1px;
  }
  .back-sub {
    position: absolute; left: 0; right: 0; top: 182px; text-align: center;
  }
  .back-sub__mark {
    display: inline-flex; align-items: center; gap: 10px;
    font-size: 22px; color: var(--brand-green-light);
  }
  .back-sub__dot { width: 14px; height: 14px; border-radius: 50%; background: var(--brand-green-light); }
  .url-bands { position: absolute; left: 0; bottom: 0; width: 540px; height: 90px; }
  .url { position: absolute; color: #fff; font-weight: 700; font-size: 15px; line-height: 17px; }
  .url--sub { left: 30px; bottom: 8px; }
  .url--main { right: 18px; bottom: 42px; }
</style>
</head>
<body>

<section class="card card--front" aria-label="Vorderseite">
  <div class="rule rule--blue" style="left:200px; top:48px; width:30px;"></div>
  <div class="rule rule--grey" style="left:200px; top:54px; width:30px;"></div>
  <div class="rule rule--blue" style="left:400px; top:48px; width:140px;"></div>
  <div class="rule rule--grey" style="left:400px; top:54px; width:140px;"></div>
  <div class="rule rule--blue" style="left:0; top:130px; width:30px;"></div>
  <div class="rule rule--grey" style="left:0; top:136px; width:30px;"></div>

  <div class="front-brand">
    <div class="front-brand__mark">Wachwechselpunkt</div>
    <div class="front-brand__company">KLO GmbH</div>
  </div>

  <div class="person">
    <div class="person__name">Jonas Berger</div>
    <div class="person__title">Geschäftsführer</div>
  </div>

  <div class="address">Lindenweg 7<br>86650 Feldau</div>

  <table class="contact">
    <tr><td class="contact__label">Telefon.:</td><td>08431 - 552 30 17</td></tr>
    <tr><td class="contact__label">Mobil.:</td><td>0176 - 318 22 905</td></tr>
    <tr><td class="contact__label">E.:</td><td>jonas.berger@wachwechselpunkt.de</td></tr>
    <tr><td class="contact__label contact__label--green">E.:</td><td>jonas.berger@marvento.de</td></tr>
  </table>

  <div class="sub-brand">
    <div class="sub-brand__mark"><span>MARVENTO</span><span class="sub-brand__dot"></span></div>
    <div class="sub-brand__site">Marvento.de</div>
    <div class="sub-brand__note">ist eine Marke der KLO GmbH</div>
  </div>
</section>

<section class="card card--back" aria-label="Rückseite">
  <div class="rule rule--blue" style="left:0; top:150px; width:540px;"></div>
  <div class="rule rule--grey" style="left:0; top:157px; width:540px;"></div>

  <div class="back-brand">Wachwechselpunkt</div>
  <div class="back-sub">
    <div class="back-sub__mark"><span>MARVENTO</span><span class="back-sub__dot"></span></div>
  </div>

  <svg class="url-bands" viewBox="0 0 540 90" aria-hidden="true">
    <polygon points="0,56 240,56 232,90 0,90" fill="var(--brand-green)"/>
    <polygon points="248,56 262,56 254,90 240,90" fill="var(--brand-grey)"/>
    <polygon points="268,56 282,56 274,90 260,90" fill="var(--brand-grey)"/>
    <polygon points="288,56 302,56 294,90 280,90" fill="var(--brand-grey)"/>
    <polygon points="314,22 540,22 540,56 306,56" fill="var(--brand-blue)"/>
  </svg>
  <div class="url url--main">www.wachwechselpunkt.de</div>
  <div class="url url--sub">www.marvento.de</div>
</section>

</body>
</html>
```